Pool Website

Need a simple front page and one internal page for a pool construction website. Please read the Must Have section for info. We uploaded 2 logos, one with color and one black and white. The colors you use in the logo can be changed, we used Century Gothic for the typing under the logo.

Nice clean design. The main back behind the site can be any color but we want the content back ground to be white.

We want a scrolling photo gallery (it doesn't have to scroll in your sample just know that's what we are envisioning) on the front page and the menu, and maybe a couple of photos down below to be clicked on such as this http://www.dellmorepools.example/

The 2ndary page would still have a header and menu and some type of cool design. Could be similar to this http://www.dellmorepools.example/about-us/awards.html

Also some other designs they like are here http://www.trelvacraft.example/14-examples-of-clean-modern-website-design-inspiration/ I realize not all of these could have a image scroller on the front page which is fine.

Please do not copy their site exactly though it must be different.

For now you can just use sample stock photography for your photos for the design but ultimately we will swap them out for our own photos so there will not be a need to purchase stock photography of pools.

Menus will include Home - About - Services - Gallery - Contact - Blog

The current site is http://www.gilesfentonpools.example/ we do not want it to look anything like this. It's way too dark and just not professional looking. We want this new site to look very slick and professional.

We also want a space for social networking logos etc.

I have also attached 2 zip files that contain photos that may be used in the design. You do not have to use them all but you are welcome to use a few. Most will be put in the photo gallery.

Colors: Blues, white, grays, black, etc.
Updates

Added several photos that can be used in the design. Obviously you do not have to use them all most will be in the photo gallery but you're welcome to use some for your design. 

Target Market(s)

People with money for residential pools or companies that want corporate pools. Are target location is Miami and California

Industry/Entity Type

Construction

Font styles to use
Serif
Sans Serif

Requirements
Must have
• Nice clean design. The main back behind the site can be any color but we want the content back ground to be white.

```html
<!DOCTYPE html>
<html lang="en">
<head>
<meta charset="utf-8">
<title>Giles Fenton Pools</title>
<link rel="stylesheet" href="https://fonts.googleapis.com/css2?family=Oswald:wght@500;600&family=Montserrat:wght@400;600&family=Alfa+Slab+One&family=Kaushan+Script&family=Roboto:wght@400&display=swap">
<style>
:root{
  --navy:#1b2a78;
  --sky-top:#eafcff;
  --sky-bottom:#a8ecf7;
  --blue:#1aa3f0;
  --blue-dark:#0a7fd8;
  --page:#f4f4f4;
  --band:#d6d6d6;
  --footer:#262626;
  --footer-bar:#3a3a3a;
  --text:#555;
  --red:#d0211c;
  --white:#fff;
}
*{box-sizing:border-box;margin:0;padding:0}
html,body{width:1200px;height:1095px;overflow:hidden}
body{position:relative;background:var(--page);font-family:"Montserrat",sans-serif;color:var(--text)}
.header{position:absolute;left:0;top:0;width:1200px;height:120px;background:linear-gradient(var(--sky-top),var(--sky-bottom))}
.brand{position:absolute;left:170px;top:38px;display:flex;align-items:center;gap:10px;font-family:"Montserrat",sans-serif;font-weight:600;font-size:18px;color:var(--navy)}
.brand-mark{width:34px;height:34px;background:var(--navy);border-radius:6px}
.social{position:absolute;left:811px;top:12px;display:flex;gap:5px}
.social span{width:32px;height:32px;border-radius:50%;background:#9aa3ad;border:2px solid #c9d0d6}
.nav{position:absolute;left:673px;top:83px;display:flex;font-family:"Oswald",sans-serif;font-weight:500;font-size:14px}
.nav a{color:var(--navy);text-decoration:none;padding:3px 10px;margin-right:6px;line-height:18px}
.nav a.active{background:var(--navy);color:var(--white)}
.slider{position:absolute;left:161px;top:135px;width:878px;height:313px;border:2px solid #fff;box-shadow:0 0 0 1px #ccc}
.slide-photo{width:100%;height:100%;background:radial-gradient(ellipse at 55% 60%,#7fd3e8,#3ea6c8 45%,#5b7a4a 80%,#2f3d22)}
.dots{position:absolute;left:400px;bottom:9px;display:flex;gap:6px}
.dots span{width:14px;height:14px;background:#fff;border:1px solid #ccc}
.dots span.on{background:#9b1d1d}
.welcome{position:absolute;left:162px;top:482px;width:610px}
.welcome h1{font-size:16px;font-weight:600;color:var(--navy);margin-bottom:3px}
.welcome p{font-size:10.5px;line-height:15.5px;color:#666}
.welcome .more{display:block;text-align:right;font-size:9px;color:var(--red);margin-top:8px;text-decoration:none}
.call{position:absolute;left:792px;top:477px;width:244px;height:72px;background:linear-gradient(var(--blue),var(--blue-dark));border:2px solid #d9eefc;border-radius:4px;color:#fff}
.call svg{position:absolute;left:22px;top:10px}
.call .label{position:absolute;left:78px;top:3px;font-family:"Kaushan Script",cursive;font-size:20px}
.call .number{position:absolute;left:62px;top:26px;font-family:"Oswald",sans-serif;font-weight:600;font-size:30px;letter-spacing:-.5px}
.band{position:absolute;left:0;top:583px;width:1200px;height:305px;background:var(--band)}
.card{position:absolute;top:598px;width:207px;height:270px;border:1px solid #eee;overflow:hidden;color:#fff}
.card-head{height:47px;background:linear-gradient(var(--blue),var(--blue-dark));font-family:"Alfa Slab One",serif;font-size:22px;text-align:center;line-height:47px;text-shadow:1px 1px 2px rgba(0,0,0,.4)}
.card-photo{position:absolute;left:0;right:0;bottom:0}
.card-body{position:absolute;left:8px;top:66px;right:6px;font-family:"Alfa Slab One",serif;font-size:16px;line-height:17px;text-shadow:1px 1px 2px rgba(0,0,0,.5)}
.card-body li{list-style:none;margin-bottom:9px;padding-left:16px;position:relative}
.card-body li::before{content:"";position:absolute;left:0;top:3px;width:11px;height:11px;background:#f5c531;clip-path:polygon(50% 0,62% 38%,100% 38%,69% 60%,80% 100%,50% 75%,20% 100%,31% 60%,0 38%,38% 38%)}
.why{font-family:"Montserrat",sans-serif;font-size:14px;line-height:15px;top:34px;color:#111;text-shadow:none}
.why p{margin-bottom:6px}
.offer-title{position:absolute;left:0;right:0;top:4px;text-align:center;font-family:"Kaushan Script",cursive;font-size:18px;color:var(--navy)}
.offer-main{position:absolute;left:0;right:0;top:108px;text-align:center;font-family:"Oswald",sans-serif;font-weight:600;font-size:24px;line-height:28px;text-shadow:1px 1px 3px rgba(0,0,0,.6)}
.pill{position:absolute;left:9px;right:9px;height:50px;background:linear-gradient(var(--blue),var(--blue-dark));border:2px solid #e5f5ff;border-radius:5px;text-align:center;font-family:"Alfa Slab One",serif;font-size:15px;line-height:17px;padding-top:7px}
.footer{position:absolute;left:0;top:888px;width:1200px;height:177px;background:var(--footer)}
.footer h2{position:absolute;top:16px;font-family:"Roboto",sans-serif;font-weight:400;font-size:22px;color:var(--blue)}
.address{position:absolute;left:160px;top:51px;font-family:"Roboto",sans-serif;font-size:14px;line-height:23px;color:#fff}
.divider{position:absolute;left:481px;top:55px;width:1px;height:90px;background:#444}
.field{position:absolute;width:208px;height:26px;border:1px solid #555;font-family:"Roboto",sans-serif;font-size:10.5px;color:#bbb;padding:6px 10px}
.send{position:absolute;left:831px;top:119px;width:94px;height:26px;background:var(--blue);border:1px solid #fff;color:#fff;font-family:"Roboto",sans-serif;font-size:14px;text-align:center;line-height:24px}
.copyright{position:absolute;left:0;top:1065px;width:1200px;height:30px;background:var(--footer-bar);text-align:center;line-height:30px;font-size:10px;color:#888}
</style>
</head>
<body>
<header class="header">
  <div class="brand"><span class="brand-mark"></span>Giles Fenton Pools</div>
  <div class="social" aria-label="Social networks"><span></span><span></span><span></span><span></span><span></span><span></span></div>
  <nav class="nav"><a class="active">HOME</a><a>ABOUT</a><a>SERVICES</a><a>GALLERY</a><a>CONTACT</a><a>BLOG</a></nav>
</header>

<section class="slider">
  <div class="slide-photo" role="img" aria-label="Photo of a free-form pool with fountain planters and palm trees"></div>
  <div class="dots"><span class="on"></span><span></span><span></span><span></span></div>
</section>

<section class="welcome">
  <h1>welcome to Giles Fenton Pool</h1>
  <p>Lorem Ipsum. Proin gravida nibh vel velit auctor aliquet. Aenean sollicitudin, lorem quis bibendum auctor, nisi elit consequat ipsum, nec sagittis sem nibh id elit. Duis sed odio sit amet nibh vulputate cursus a sit amet mauris. Morbi accumsan ipsum velit. Nam nec tellus a odio tincidunt auctor a ornare odio. Sed non&nbsp; mauris vitae erat consequat auctor</p>
  <a class="more">Learn more</a>
</section>

<div class="call">
  <svg width="40" height="56" viewBox="0 0 40 56"><path d="M34 6 C10 2 2 22 10 34 C14 40 20 42 22 44" fill="none" stroke="#d0211c" stroke-width="4"/><path d="M14 40 L24 46 L16 54" fill="none" stroke="#d0211c" stroke-width="4"/></svg>
  <span class="label">Call us now</span>
  <span class="number">555-014-0297</span>
</div>

<div class="band"></div>

<article class="card" style="left:161px">
  <div class="card-photo" style="top:0;background:linear-gradient(#bfe3f5 0%,#8fc4dc 30%,#3d7fa0 55%,#5db7d8 100%)" role="img" aria-label="Photo of a pool waterfall wall under a blue sky"></div>
  <div class="offer-title">Special Offer!</div>
  <div class="offer-main">FREE ESTIMATES &amp;<br>DESIGN CONSULTS</div>
  <div class="pill" style="top:198px">Lifetime Warranty<br>Available</div>
</article>

<article class="card" style="left:384px">
  <div class="card-head">Our Services</div>
  <div class="card-photo" style="top:47px;background:linear-gradient(160deg,#8fc6c4,#3f8fa8 50%,#2c6f8e)" role="img" aria-label="Photo of pool water beside a stone deck"></div>
  <ul class="card-body">
    <li>Commercial Pool Installation</li><li>Pool Maintenance</li><li>Pool Remodeling</li><li>Pool Renovation</li><li>Swimming Pool Installation</li><li>Pool Repair</li>
  </ul>
</article>

<article class="card" style="left:608px">
  <div class="card-head">Why Choose Us</div>
  <div class="card-photo" style="top:47px;background:linear-gradient(160deg,#d4f0f3,#9ad8e4 50%,#c9ecef)" role="img" aria-label="Photo of bright turquoise pool water"></div>
  <div class="card-body why" style="top:80px">
    <p>Free Estimates</p><p>Family Owned since 1979</p><p>Coastal Pool Builders Guild Member</p><p>Awarded over 75 CPBG Awards</p><p>Free Design Consults Available</p>
  </div>
</article>

<article class="card" style="left:831px">
  <div class="card-head">Our Gallery</div>
  <div class="card-photo" style="top:47px;background:linear-gradient(#6f8a5a,#a9b7ae 35%,#3f7fa3 65%,#6fb6d0)" role="img" aria-label="Photo of a tiled fountain pool with planter urns in a garden"></div>
  <div class="pill" style="top:204px">Click to view<br>Our Gallery</div>
</article>

<footer class="footer">
  <h2 style="left:160px">Contact Info</h2>
  <div class="address">Giles Fenton Pools Showroom<br>Located at 2280 Harbor Court,<br>Seabright, Florida 33070</div>
  <div class="divider"></div>
  <h2 style="left:607px">Contact Us</h2>
  <div class="field" style="left:608px;top:56px">Enter your name</div>
  <div class="field" style="left:608px;top:88px">Enter your email</div>
  <div class="field" style="left:608px;top:119px">Enter your Phone Number</div>
  <div class="field" style="left:831px;top:56px;height:57px">Enter your Questions / Comments</div>
  <div class="send">Send</div>
</footer>
<div class="copyright">Copyright © 2014 Giles Fenton Pools, All rights reserved</div>
</body>
</html>
```